Valdarossi’s Artisan Pizzeria Menu Contest

I’m looking for a menu design for a new pizzeria - it’s farm to table type of restaurant - more upscale than a typical pizzeria - white washed wood interior with some industrial accents - I am looking for a creative menu layout using the attached sample menu items -
Valdarossi’s is an artisanal pizzeria with an atmosphere that will make you feel at home for any situation, first date, anniversary, business lunch, boys night out or girls night out with a menu inspired by the idea of a simple honest cooking paired with fresh – quality ingredients. Full service dining experience that is still casual but dedicated to extraordinary hospitality.
While developing the menu we have created a network of amazing farms and purveyors to supply our restaurant with fresh milled 100% California flour for our hand crafted dough, as well as sustainably farmed organic produce, meats and cheeses.
The menu includes classics like the Margherita pizza to daily seasonal specials, fresh salads to rustic small plates including moms meatball recipe to a fresh local burrata with handmade bread. Each dish reflects our passion for sourcing the freshest quality local ingredients.
To compliment the menu, Valdarossi’s serves an extensive wine list with selections focusing on Italian varietals. The cocktail program has been carefully crafted to offer something to entice ever palate and the beer list has unique selections of the world’s finest brewers.
Target Market(s)
25-45 year old men and women
Industry/Entity Type
American Restaurant
Requirements
Must have
- professional tone
Nice to have
- a balance of elegance and industrial (rustic)
Should not have
- photos or playful graphics etc..

```html
<!DOCTYPE html>
<html lang="en">
<head>
<meta charset="utf-8">
<title>Valdarossi’s Menu</title>
<link href="https://fonts.googleapis.com/css2?family=Playfair+Display:ital,wght@0,400;0,700;0,900;1,400&display=swap" rel="stylesheet">
<style>
:root{
  --page:#ffffff;
  --paper:#f1ede3;
  --paper-edge:#e8e2d5;
  --ink:#1a1a1a;
  --soft-ink:#2c2c2c;
  --red:#e84a4b;
}
*{margin:0;padding:0;box-sizing:border-box}
html,body{width:916px;height:1200px;overflow:hidden;background:var(--page)}
.canvas{position:relative;width:916px;height:1200px;font-family:"Playfair Display",Georgia,serif;color:var(--ink)}
.paper{position:absolute;left:92px;top:83px;width:732px;height:1037px;
  background:radial-gradient(ellipse at 55% 40%,var(--paper) 0%,var(--paper) 55%,var(--paper-edge) 100%)}
.brand{position:absolute;left:189px;top:601px;transform:translate(-50%,-50%) rotate(90deg);
  font-size:40px;font-weight:400;letter-spacing:3px;color:var(--ink);white-space:nowrap}
.section-title{position:absolute;display:flex;align-items:center;gap:6px;height:26px}
.section-title h2{font-size:24px;font-weight:900;line-height:1;white-space:nowrap;letter-spacing:-.2px}
.section-title .bar{flex:1;height:10px;margin-top:4px;
  background:linear-gradient(115deg,var(--red) 0 34px,var(--ink) 34px)}
.col-left{left:285px;width:246px}
.col-right{left:551px;width:246px}
.item{position:absolute}
.item-row{display:flex;justify-content:space-between;align-items:baseline;
  border-bottom:1px dotted #6a6a6a;padding-right:16px;height:18px}
.item-name{font-size:15.5px;font-weight:400;line-height:18px;white-space:nowrap}
.item-price{font-size:12px;font-weight:700}
.item-price small{font-size:8px}
.item-desc{font-size:8.8px;font-style:italic;line-height:11px;margin-top:2px;color:var(--soft-ink);padding-right:40px}
</style>
</head>
<body>
<div class="canvas">
  <div class="paper"></div>
  <div class="brand">Valdarossi’s</div>

  <!-- Left column -->
  <div class="section-title col-left" style="top:151px"><h2>Pizzas</h2><span class="bar"></span></div>
  <div class="item col-left" style="top:179px"><div class="item-row"><span class="item-name">Margherita</span><span class="item-price"><small>$</small>14</span></div><p class="item-desc">Classic margherita pizza – fresh mozz<br>tomato sauce and basil</p></div>
  <div class="item col-left" style="top:233px"><div class="item-row"><span class="item-name">Organic Sausage</span><span class="item-price"><small>$</small>16</span></div><p class="item-desc">Organic sausage housemade red<br>sauce mozz hint of fennel</p></div>
  <div class="item col-left" style="top:286px"><div class="item-row"><span class="item-name">Pepperoni</span><span class="item-price"><small>$</small>16</span></div><p class="item-desc">Hollis Pepperoni – Housemade Red<br>Sauce Chile flakes and Mozz</p></div>
  <div class="item col-left" style="top:338px"><div class="item-row"><span class="item-name">Salumi and Burrata</span><span class="item-price"><small>$</small>17</span></div><p class="item-desc">Salumi dried red sauce finished with<br>whipped burrata</p></div>
  <div class="item col-left" style="top:390px"><div class="item-row"><span class="item-name">Daily Special</span><span class="item-price"><small>$</small>17</span></div></div>
  <div class="item col-left" style="top:420px"><div class="item-row"><span class="item-name">Mushroom</span><span class="item-price"><small>$</small>15</span></div><p class="item-desc">Shaved mushrooms with a parmesan<br>cream and melted onions</p></div>
  <div class="item col-left" style="top:470px"><div class="item-row"><span class="item-name">Prosciutto And Egg</span><span class="item-price"><small>$</small>16</span></div><p class="item-desc">Parma Prosciutto Parmesan cream with Fjordberg<br>and gruyere finished with an organic egg</p></div>
  <div class="item col-left" style="top:523px"><div class="item-row"><span class="item-name">Quarttro Formaggi</span><span class="item-price"><small>$</small>15</span></div><p class="item-desc">Four cheese combination – mozz – fontina –<br>parm cream and gruyere chile flakes and oregano</p></div>
  <div class="item col-left" style="top:580px"><div class="item-row"><span class="item-name">Farmers Pizza</span><span class="item-price"><small>$</small>17</span></div><p class="item-desc">Seasonal vegatables cream sauce and a<br>variety of cheese</p></div>
  <div class="item col-left" style="top:635px"><div class="item-row"><span class="item-name">Keto Friendly</span><span class="item-price"><small>$</small>17</span></div><p class="item-desc">Cauliflower crust, spinach and kale ,<br>parm cream sauce</p></div>

  <div class="section-title col-left" style="top:694px"><h2>Crusts</h2><span class="bar"></span></div>
  <div class="item col-left" style="top:723px"><div class="item-row"><span class="item-name">Traditional</span><span class="item-price"><small>$</small></span></div><p class="item-desc">Orginal crust you can't miss</p></div>
  <div class="item col-left" style="top:772px"><div class="item-row"><span class="item-name">Gluten Free</span><span class="item-price"><small>$</small>3</span></div><p class="item-desc">Best gluten friendly crust on the west coast</p></div>
  <div class="item col-left" style="top:813px"><div class="item-row"><span class="item-name">Cauliflower</span><span class="item-price"><small>$</small>3</span></div><p class="item-desc">Vegans have needs</p></div>

  <div class="section-title col-left" style="top:863px"><h2>Dips</h2><span class="bar"></span></div>
  <div class="item col-left" style="top:900px"><div class="item-row"><span class="item-name">Ranch</span><span class="item-price"><small>$</small>1</span></div></div>
  <div class="item col-left" style="top:925px"><div class="item-row"><span class="item-name">Tomato Sauce</span><span class="item-price"><small>$</small>1</span></div></div>
  <div class="item col-left" style="top:949px"><div class="item-row"><span class="item-name">Spicy Dip</span><span class="item-price"><small>$</small>1</span></div></div>
  <div class="item col-left" style="top:974px"><div class="item-row"><span class="item-name">Blue Cheese</span><span class="item-price"><small>$</small>1</span></div></div>

  <div class="section-title col-left" style="top:1014px"><h2>Daily Soup</h2><span class="bar"></span></div>
  <div class="item col-left" style="top:1041px"><div class="item-row"><span class="item-name">Tomato Bisque</span><span class="item-price"><small>$</small>8</span></div></div>

  <!-- Right column -->
  <div class="section-title col-right" style="top:151px"><h2>Sandwiches</h2><span class="bar"></span></div>
  <div class="item col-right" style="top:179px"><div class="item-row"><span class="item-name">Italian Sub</span><span class="item-price"><small>$</small>13</span></div><p class="item-desc">Prociutto, salumi, turkey, provolone, lettuce,<br>tomato and herb aioli with spicy gardenia</p></div>
  <div class="item col-right" style="top:236px"><div class="item-row"><span class="item-name">Turkey Sandwich</span><span class="item-price"><small>$</small>12</span></div><p class="item-desc">Housemade bread – turkey, cheddar cheese,<br>butter lettuce, tomato and mustard aioli</p></div>
  <div class="item col-right" style="top:289px"><div class="item-row"><span class="item-name">Meatball Sub</span><span class="item-price"><small>$</small>13</span></div><p class="item-desc">Moms meatballs melted provolone on a<br>housemade roll</p></div>
  <div class="item col-right" style="top:340px"><div class="item-row"><span class="item-name">Plantwise Burger</span><span class="item-price"><small>$</small>14</span></div><p class="item-desc">Housemade bun – arugula , tomato, onion and a<br>sundried tomato spread</p></div>
  <div class="item col-right" style="top:390px"><div class="item-row"><span class="item-name">Chicken Sandwich</span><span class="item-price"><small>$</small>13</span></div><p class="item-desc">Fried chicken or chicken breast, provolone, argula,<br>tomato, served with a spicy aioli</p></div>

  <div class="section-title col-right" style="top:454px"><h2>Appetizers</h2><span class="bar"></span></div>
  <div class="item col-right" style="top:487px"><div class="item-row"><span class="item-name">Brussels</span><span class="item-price"><small>$</small>10</span></div><p class="item-desc">Pan seared brussel sprouts with a drizzle of<br>balsamic reduction and parm and bread crumbs</p></div>
  <div class="item col-right" style="top:543px"><div class="item-row"><span class="item-name">Meatballs</span><span class="item-price"><small>$</small>13</span></div><p class="item-desc">Moms meatballs handmade secret recipe for<br>over 75 years</p></div>
  <div class="item col-right" style="top:596px"><div class="item-row"><span class="item-name">Mussels</span><span class="item-price"><small>$</small>15</span></div><p class="item-desc">New Zealand Mussels in a tomato broth</p></div>
  <div class="item col-right" style="top:637px"><div class="item-row"><span class="item-name">Romanesco</span><span class="item-price"><small>$</small>11</span></div><p class="item-desc">Flash fried romanesco served atop a spicy aioli</p></div>
  <div class="item col-right" style="top:679px"><div class="item-row"><span class="item-name">Chicken wings</span><span class="item-price"><small>$</small>10</span></div><p class="item-desc">Italian fried chicken wings with a kick</p></div>
  <div class="item col-right" style="top:720px"><div class="item-row"><span class="item-name">Burrata</span><span class="item-price"><small>$</small>13</span></div><p class="item-desc">Local burrata served with apples grapes and<br>fresh made bread</p></div>

  <div class="section-title col-right" style="top:781px"><h2>Salads</h2><span class="bar"></span></div>
  <div class="item col-right" style="top:809px"><div class="item-row"><span class="item-name">Chopped Salad</span><span class="item-price"><small>$</small>13</span></div><p class="item-desc">Lettuce mix with tomato, onions, peppers,<br>pepperoni, chick peas, fresh mozz, italian herb ving</p></div>
  <div class="item col-right" style="top:865px"><div class="item-row"><span class="item-name">Caesar Salad</span><span class="item-price"><small>$</small>11</span></div><p class="item-desc">Traditional caesar salad rich and creamy extra<br>shaved parmesan</p></div>
  <div class="item col-right" style="top:921px"><div class="item-row"><span class="item-name">Farm Salad</span><span class="item-price"><small>$</small>15</span></div><p class="item-desc">Seasonal farmers market salad</p></div>
  <div class="item col-right" style="top:962px"><div class="item-row"><span class="item-name">Grilled Little Gem</span><span class="item-price"><small>$</small>11</span></div><p class="item-desc">Grilled little gems with bacon, tomato, red onions<br>and blue cheese dressing</p></div>
  <div class="item col-right" style="top:1012px"><div class="item-row"><span class="item-name">Spinach and Arugula Salad</span><span class="item-price"><small>$</small>12</span></div><p class="item-desc">Spinach and argula, red pepperstossed in a lemon<br>ving and housemade croutons</p></div>
</div>
</body>
</html>
```